Lumen Forge Unique Marketing Website Design

I am starting a new company that is a thought leader in the marketing consulting space. The company is called Lumen Forge. We intend to build a Wordpress site on the Astra Theme with the Spectra builder. Our goal is to become the leading voice that empowers high-ticket service business leaders to become Lumen Forge by equipping them with the cutting-edge frameworks and decision grade intelligence taught in leading business schools. What we are looking for is a website design that is clean and professional, making some use of white space well also being eye catching and distinctive in the consulting space. We will probably want to have a video on the homepage not in the hero section, but just below to explain the company and what we do. Our tagline is "Be found. Be chosen." I have attached a brand guide with some messaging, our typography choices, and our color system. The full site will have a primary nav that is four pages - About us, Services, Insights (essentially a blog), and Contact Us. The goal of this project is to develop an art direction that I can give to a designer to build loads of new pages.

Target Market(s)

Business owners (mostly male) from 30-60 years old, looking to fix their sales and marketing funnel.

Industry/Entity Type

Marketing consulting

Font styles to use
Sans Serif

Requirements
Must have
• A clean, professional design that builds trust with owners of high-ticket service businesses. We need a space for explainer video, and sections that tell prospects what we do. Would also like to have a blog carousel.
Nice to have
• Social feeds, if possible. See attached documents for colors and fonts.
Should not have
• Our feel is professional enough to be trustworthy, but unique enough to be memorable. Cartoon ideas do not meet the professional test, and we do not want the website to appear feminine.

```html
<!DOCTYPE html>
<html lang="en">
<head>
<meta charset="utf-8">
<title>Lumen Forge — Be Found. Be Chosen.</title>
<link href="https://fonts.googleapis.com/css2?family=Inter:wght@400;500;600;700&display=swap" rel="stylesheet">
<style>
:root{
  --ink:#1c1d22;
  --muted:#4a4c55;
  --blue:#2d5bff;
  --navy:#1b2246;
  --navy-deep:#141a38;
  --paper:#ffffff;
  --mist:#f4f4f5;
  --line:#e3e4e8;
}
*{box-sizing:border-box;margin:0;padding:0}
html,body{width:694px;height:1200px;overflow:hidden}
body{font-family:'Inter',sans-serif;color:var(--ink);background:var(--paper);position:relative}
.abs{position:absolute}

/* header */
.site-header{position:absolute;left:0;top:0;width:694px;height:40px;background:var(--paper)}
.brand{left:72px;top:12px;font-size:12px;font-weight:700;letter-spacing:.2px;color:var(--ink)}
.main-nav{top:15px;font-size:7.2px;color:var(--ink)}
.main-nav.active{color:var(--blue)}
.call{left:487px;top:13px}
.call-label{left:499px;top:12px;font-size:5.4px;font-weight:500}
.call-number{left:499px;top:20px;font-size:6.6px;font-weight:700;letter-spacing:-.2px}
.quote-btn{left:565px;top:9px;width:57px;height:23px;border-radius:12px;background:var(--blue);color:#fff;font-size:5.8px;display:flex;align-items:center;justify-content:center}

/* hero */
.hero{left:0;top:40px;width:694px;height:381px;background:linear-gradient(120deg,#232b52 0%,var(--navy) 45%,#1e2650 100%)}
.tag{display:flex;align-items:center;gap:4px;height:12px;padding:0 5px;border:1px solid rgba(255,255,255,.35);border-radius:7px;font-size:4.2px;letter-spacing:.5px;font-weight:500;color:#fff}
.tag::before{content:"";width:2.4px;height:2.4px;border-radius:50%;background:var(--blue)}
.tag.light{color:var(--ink);border-color:var(--line)}
.hero-title{left:70px;top:130px;font-size:48px;line-height:48px;font-weight:400;color:#fff;letter-spacing:-.5px}
.hero-title .accent{color:var(--blue)}
.hero-copy{left:70px;width:240px;font-size:7.2px;line-height:11.6px;color:#fff}
.insights-btn{left:70px;top:343px;width:92px;height:24px;border:1px solid rgba(255,255,255,.8);border-radius:12px;color:#fff;font-size:5.8px;display:flex;align-items:center;padding-left:16px}
.insights-btn .dot{position:absolute;right:4px;top:3.5px;width:16px;height:16px;border-radius:50%;background:var(--blue);display:flex;align-items:center;justify-content:center}
.scroll-dot{left:337px;top:382px;width:19px;height:19px;border-radius:50%;background:#fff;display:flex;align-items:center;justify-content:center}
.stat-card{left:430px;top:266px;width:113px;height:124px;border-radius:8px;border:1px solid rgba(255,255,255,.15);background:rgba(30,38,78,.85);color:#fff;padding:16px}
.stat-num{font-size:18px;font-weight:400}
.stat-label{font-size:6.2px;font-weight:500;margin-top:6px}
.stat-text{font-size:5.6px;line-height:10.2px;margin-top:23px}
.team-photo{left:550px;top:266px;width:113px;height:124px;border-radius:8px;background:linear-gradient(150deg,#e8ebf0,#b7a58a 55%,#3b3f52)}

/* problem */
.problem{left:0;top:421px;width:694px;height:331px;background:var(--mist)}
.problem-title{left:64px;top:482px;font-size:30px;font-weight:400;letter-spacing:-.3px}
.problem-title .accent{color:var(--blue)}
.problem-sub{left:64px;top:526px;font-size:20.5px;font-weight:400}
.pain-card{top:580px;width:161px;height:94px;background:var(--paper);border-radius:6px;padding:16px 17px}
.pain-card p{font-size:11.4px;line-height:13.2px;font-weight:400}
.pain-card .rule{position:absolute;left:17px;bottom:16px;height:1px;background:var(--line)}
.problem-note{left:64px;top:694px;font-size:6.7px;line-height:10.2px;color:var(--muted)}
.problem-note strong{color:var(--ink);font-weight:600}

/* system */
.system-tag{left:307px;top:796px}
.system-title{left:0;top:811px;width:694px;text-align:center;font-size:24px;line-height:27px;font-weight:400}
.system-title .accent{color:var(--blue)}
.video{left:64px;top:888px;width:566px;height:258px;border-radius:12px;background:linear-gradient(135deg,#3b3a3d 0%,#2a2a2e 45%,#1a1b20 100%);overflow:hidden}
.play{left:272px;top:116px}
.video-tools{right:8px;bottom:6px;display:flex;gap:8px}
</style>
</head>
<body>

<header class="site-header">
  <div class="abs brand">LUMEN FORGE</div>
  <span class="abs main-nav active" style="left:259px">Home</span>
  <span class="abs main-nav" style="left:293px">About Us</span>
  <span class="abs main-nav" style="left:337px">Services</span>
  <span class="abs main-nav" style="left:380px">Blog</span>
  <span class="abs main-nav" style="left:408px">Contact</span>
  <svg class="abs call" width="10" height="10" viewBox="0 0 24 24" fill="none" stroke="#1c1d22" stroke-width="1.6"><path d="M5 3h4l2 5-2.5 1.5a11 11 0 0 0 6 6L16 13l5 2v4a2 2 0 0 1-2 2A16 16 0 0 1 3 5a2 2 0 0 1 2-2z"/></svg>
  <span class="abs call-label">Call Us Phone</span>
  <span class="abs call-number">(+100) 555 014 200</span>
  <a class="abs quote-btn">Get A Quote</a>
</header>

<section class="abs hero">
  <div role="img" aria-label="Overhead photo of a business team meeting around a table, dark blue overlay" style="position:absolute;inset:0;background:radial-gradient(ellipse at 40% 35%,rgba(60,70,110,.35),transparent 60%)"></div>
</section>
<div class="abs tag" style="left:70px;top:112px">FAST AND RELIABLE</div>
<h1 class="abs hero-title">Be Found.<br>Be <span class="accent">Chosen</span>.</h1>
<p class="abs hero-copy" style="top:244px">Decision-grade intelligence and buyer psychology for high-ticket service businesses that want to get chosen more often—without pressure, gimmicks, or guesswork.</p>
<p class="abs hero-copy" style="top:290px">Most businesses focus on lead generation at the top and closing at the bottom. The real problem lives in the black box in between—where trust breaks down, motivation leaks, and deals quietly die.</p>
<a class="abs insights-btn">Read Our Insights<span class="dot"><svg width="7" height="7" viewBox="0 0 10 10" fill="none" stroke="#fff" stroke-width="1.3"><path d="M2 8L8 2M3.5 2H8v4.5"/></svg></span></a>
<div class="abs scroll-dot"><svg width="7" height="7" viewBox="0 0 10 10" fill="none" stroke="#2d5bff" stroke-width="1.2"><path d="M5 1v8M2 6l3 3 3-3"/></svg></div>
<div class="abs stat-card">
  <div class="stat-num">260+</div>
  <div class="stat-label">Successful Projects</div>
  <div class="stat-text">Lumen Forge Exists To Illuminate That Black Box And Redesign How Buyers Decide.</div>
</div>
<div class="abs team-photo" role="img" aria-label="Photo of a team collaborating around a laptop in a bright office"></div>

<section class="abs problem"></section>
<h2 class="abs problem-title">The Problem Isn’t Your <span class="accent">Leads</span>.</h2>
<p class="abs problem-sub">It’s What Happens After They Raise Their Hand.</p>
<div class="abs pain-card" style="left:6px"><p>Deals slow<br>down for “no<br>clear reason”</p><span class="rule" style="width:128px"></span></div>
<div class="abs pain-card" style="left:180px"><p>Prospects ghost<br>after good<br>conversations</p><span class="rule" style="width:101px"></span></div>
<div class="abs pain-card" style="left:353px"><p>Sales cycles<br>stretch longer than<br>they should</p><span class="rule" style="width:110px"></span></div>
<div class="abs pain-card" style="left:527px;height:92px"><p>Marketing and<br>sales argue—but<br>can’t explain why</p><span class="rule" style="width:128px"></span></div>
<p class="abs problem-note">Revenue doesn’t usually disappear at the top or bottom of the funnel.<br>It leaks in the middle—where buyers are deciding whether you’re worth trusting.<br><strong>Most companies never see it. We make it visible.</strong></p>

<div class="abs tag light system-tag">360-DEGREE PANORAMAS</div>
<h2 class="abs system-title">See <span class="accent">The Revenue System</span> Most<br>Businesses Never Learn To See</h2>
<div class="abs video" role="img" aria-label="Explainer video still: a consultant presenting an analytics dashboard to colleagues">
  <svg class="abs play" width="24" height="28" viewBox="0 0 24 28"><path d="M3 2.5Q3 1 4.4 1.8L22 12.6q1.3.9 0 1.8L4.4 25.2Q3 26 3 24.5z" fill="#fff"/></svg>
  <div class="abs video-tools">
    <svg width="9" height="9" viewBox="0 0 24 24" fill="#fff"><path d="M12 8a4 4 0 1 0 0 8 4 4 0 0 0 0-8zm9 5.5v-3l-2.4-.6-.8-1.9 1.3-2.1-2.1-2.1-2.1 1.3-1.9-.8L12.5 2h-3l-.6 2.4-1.9.8-2.1-1.3-2.1 2.1 1.3 2.1-.8 1.9L1 10.5v3l2.4.6.8 1.9-1.3 2.1 2.1 2.1 2.1-1.3 1.9.8.6 2.4h3l.6-2.4 1.9-.8 2.1 1.3 2.1-2.1-1.3-2.1.8-1.9z"/></svg>
    <svg width="9" height="9" viewBox="0 0 24 24" fill="none" stroke="#fff" stroke-width="2.4"><path d="M3 8V3h5M16 3h5v5M21 16v5h-5M8 21H3v-5"/></svg>
  </div>
</div>

</body>
</html>
```